Vantrelo App Homepage Design making customers feel in control of their spend

Hi,
We need a App Homepage design with a UI similar to the attached mock up on an Quorix 4. The app is intended to put customers in control of their usage and spend on their fixed phone, broadband, mobile, gas and electricity.

Please fee free to propose improvements to the background images, icons, colours, etc.

Any questions please let me know.

Thanks
Bertram

Target Market(s)

Consumer customers

Industry/Entity Type

Internet

Font styles to use
Sans Serif

Colors
3276b5
0255a3
85acd3
cfdeed
ffffff

Requirements
Must have
• Content in line with the guidelines in the attached mock up

```html
<!DOCTYPE html>
<html lang="en">
<head>
<meta charset="utf-8">
<title>Vantrelo App Screens</title>
<link href="https://fonts.googleapis.com/css2?family=Quicksand:wght@500;600;700&display=swap" rel="stylesheet">
<style>
  :root {
    --navy: #022a6e;
    --ink: #1c1c1c;
    --stage: #e6ebf1;
    --white: #ffffff;
    --rule: #e3e3e3;
    --band: #ececec;
    --phone: #cc1f0e;
    --broadband: #f39200;
    --mobile: #c5cc00;
    --gas: #1b9ad9;
    --donut-grey: #d3d3d3;
  }
  * { box-sizing: border-box; margin: 0; padding: 0; }
  html, body { width: 1200px; height: 1200px; overflow: hidden; }
  body {
    background: var(--stage);
    font-family: "Quicksand", sans-serif;
    color: var(--ink);
    position: relative;
  }
  .screen {
    position: absolute;
    top: 255px;
    width: 388px;
    height: 690px;
    background: var(--white);
    overflow: hidden;
    box-shadow: 0 10px 30px rgba(2, 42, 110, 0.15);
  }
  .screen--splash { left: 141px; }
  .screen--dashboard { left: 671px; }

  /* Splash */
  .splash-brand {
    position: absolute;
    top: 318px; left: 0; width: 100%;
    display: flex; align-items: center; justify-content: center; gap: 12px;
  }
  .splash-brand .dot { width: 26px; height: 26px; border-radius: 50%; background: var(--navy); }
  .splash-brand .name { font-weight: 700; font-size: 42px; color: var(--navy); letter-spacing: -0.5px; }
  .loading-bar {
    position: absolute; left: 46px; top: 567px; width: 162px; height: 2px;
    background: linear-gradient(90deg, #f7a600, #e9447a, #8e4fd1);
  }
  .loading-label {
    position: absolute; left: 146px; top: 584px; width: 100px; text-align: center;
    font-size: 12px; font-weight: 700; color: var(--navy);
  }

  /* Dashboard */
  .topbar { position: absolute; top: 0; left: 0; width: 100%; height: 58px; background: var(--navy); color: var(--white); }
  .status { position: absolute; top: 2px; left: 9px; right: 9px; height: 18px; font-size: 13px; font-weight: 600; display: flex; align-items: center; justify-content: space-between; }
  .status .left, .status .right { display: flex; align-items: center; gap: 5px; }
  .status .time { position: absolute; left: 0; right: 0; text-align: center; }
  .battery { width: 28px; height: 11px; border: 1.5px solid var(--white); border-radius: 2px; position: relative; }
  .battery::before { content: ""; position: absolute; left: 1px; top: 1px; bottom: 1px; width: 7px; background: var(--white); }
  .battery::after { content: ""; position: absolute; right: -4px; top: 2px; width: 2px; height: 4px; background: var(--white); }
  .title { position: absolute; top: 30px; left: 0; width: 100%; text-align: center; font-size: 15px; font-weight: 600; letter-spacing: 0.3px; }
  .menu { position: absolute; right: 14px; top: 31px; }

  .profile { position: absolute; top: 58px; left: 0; width: 100%; height: 84px; border-bottom: 1.5px solid var(--rule); }
  .avatar {
    position: absolute; left: 25px; top: 14px; width: 60px; height: 60px; border-radius: 50%;
    background: radial-gradient(circle at 50% 40%, #c99b80, #5a3a2c);
    border: 3px solid transparent;
    box-shadow: 0 0 0 2px #e9447a;
  }
  .greeting { position: absolute; left: 110px; top: 24px; width: 180px; text-align: center; font-size: 15px; font-weight: 600; line-height: 20px; }

  .donut { position: absolute; left: 110px; top: 168px; }
  .donut-label { position: absolute; left: 144px; top: 220px; width: 100px; text-align: center; }
  .donut-label .count { font-size: 24px; font-weight: 600; line-height: 28px; }
  .donut-label .caption { font-size: 15px; font-weight: 600; }

  .total { position: absolute; top: 358px; left: 0; width: 100%; height: 51px; border-top: 1.5px solid var(--rule); }
  .total .label { position: absolute; left: 63px; top: 16px; font-size: 15px; font-weight: 600; }
  .total .amount { position: absolute; left: 203px; top: 6px; font-size: 26px; font-weight: 700; }
  .currency { font-size: 0.55em; font-weight: 700; margin-right: 3px; }

  .charges { position: absolute; top: 409px; left: 0; width: 100%; height: 223px; background: var(--band); padding: 10px 8px 0; }
  .charge { height: 53px; background: var(--white); margin-bottom: 2px; position: relative; display: flex; align-items: center; }
  .charge:last-child { height: 48px; margin-bottom: 0; }
  .charge .icon { position: absolute; left: 14px; width: 22px; height: 22px; }
  .charge .tag { position: absolute; left: 61px; height: 25px; padding: 0 14px; color: var(--white); font-size: 15px; font-weight: 600; line-height: 25px; }
  .charge .value { position: absolute; right: 22px; font-size: 22px; font-weight: 600; }
  .tag--phone { background: var(--phone); }
  .tag--broadband { background: var(--broadband); }
  .tag--mobile { background: var(--mobile); }
  .tag--gas { background: var(--gas); }

  .footer { position: absolute; bottom: 0; left: 0; width: 100%; height: 58px; background: var(--navy); color: var(--white); font-size: 15px; font-weight: 600; }
  .footer .last-bill { position: absolute; left: 68px; top: 9px; word-spacing: 6px; }
  .footer .renewal { position: absolute; left: 70px; top: 33px; display: flex; align-items: center; gap: 8px; }
</style>
</head>
<body>

<section class="screen screen--splash">
  <div class="splash-brand"><span class="dot"></span><span class="name">Vantrelo</span></div>
  <div class="loading-bar"></div>
  <div class="loading-label">Loading</div>
</section>

<section class="screen screen--dashboard">
  <header class="topbar">
    <div class="status">
      <span class="left">●●○○○ Nexa
        <svg width="15" height="11" viewBox="0 0 15 11"><path d="M1 4a9 9 0 0 1 13 0M3.5 6.5a5.5 5.5 0 0 1 8 0" fill="none" stroke="#fff" stroke-width="1.6"/><circle cx="7.5" cy="9" r="1.5" fill="#fff"/></svg>
      </span>
      <span class="time">12:53 pm</span>
      <span class="right">31% <span class="battery"></span></span>
    </div>
    <div class="title">DASHBOARD</div>
    <svg class="menu" width="22" height="16" viewBox="0 0 22 16"><path d="M0 1h22M0 8h22M0 15h22" stroke="#fff" stroke-width="2.4"/></svg>
  </header>

  <div class="profile">
    <div class="avatar" role="img" aria-label="Profile photo of the account holder"></div>
    <p class="greeting">Good Morning Maren !<br>Welcome to Vantrelo</p>
  </div>

  <svg class="donut" width="168" height="168" viewBox="0 0 168 168">
    <g transform="rotate(-90 84 84)" fill="none" stroke-width="32">
      <circle cx="84" cy="84" r="66" stroke="var(--donut-grey)" stroke-dasharray="109.4 414.7" stroke-dashoffset="0"/>
      <circle cx="84" cy="84" r="66" stroke="var(--phone)" stroke-dasharray="28.8 414.7" stroke-dashoffset="-109.4"/>
      <circle cx="84" cy="84" r="66" stroke="var(--broadband)" stroke-dasharray="74.9 414.7" stroke-dashoffset="-138.2"/>
      <circle cx="84" cy="84" r="66" stroke="var(--mobile)" stroke-dasharray="138.2 414.7" stroke-dashoffset="-213.1"/>
      <circle cx="84" cy="84" r="66" stroke="var(--gas)" stroke-dasharray="63.4 414.7" stroke-dashoffset="-351.3"/>
    </g>
  </svg>
  <div class="donut-label"><div class="count">1</div><div class="caption">Bill Due</div></div>

  <div class="total">
    <span class="label">Total Charges</span>
    <span class="amount"><span class="currency">$</span>8,350</span>
  </div>

  <div class="charges">
    <div class="charge">
      <svg class="icon" viewBox="0 0 22 22"><path d="M2 8c0-4 18-4 18 0v2h-4V8H6v2H2z" fill="var(--phone)"/><path d="M5 11h12l2 8H3z" fill="var(--phone)"/><g fill="#fff"><rect x="8" y="13" width="2" height="1.6"/><rect x="12" y="13" width="2" height="1.6"/><rect x="8" y="16" width="2" height="1.6"/><rect x="12" y="16" width="2" height="1.6"/></g></svg>
      <span class="tag tag--phone">PHONE</span>
      <span class="value"><span class="currency">$</span>560</span>
    </div>
    <div class="charge">
      <svg class="icon" viewBox="0 0 22 22" fill="none" stroke="var(--broadband)" stroke-width="1.8"><circle cx="11" cy="11" r="9"/><ellipse cx="11" cy="11" rx="4" ry="9"/><path d="M2 11h18M4 6h14M4 16h14"/></svg>
      <span class="tag tag--broadband">BROADBAND</span>
      <span class="value"><span class="currency">$</span>2060</span>
    </div>
    <div class="charge">
      <svg class="icon" viewBox="0 0 22 22"><rect x="6" y="1" width="10" height="20" rx="2" fill="none" stroke="var(--mobile)" stroke-width="2"/><circle cx="11" cy="17.5" r="1.2" fill="var(--mobile)"/></svg>
      <span class="tag tag--mobile">MOBILE</span>
      <span class="value"><span class="currency">$</span>5285</span>
    </div>
    <div class="charge">
      <svg class="icon" viewBox="0 0 22 22"><rect x="9" y="0" width="4" height="3" fill="var(--gas)"/><rect x="5" y="3" width="12" height="19" rx="4" fill="var(--gas)"/></svg>
      <span class="tag tag--gas">GAS</span>
      <span class="value"><span class="currency">$</span>1160</span>
    </div>
  </div>

  <footer class="footer">
    <div class="last-bill">Last Bill &nbsp;$560 &nbsp;on &nbsp;09/12/2016</div>
    <div class="renewal">
      <svg width="15" height="16" viewBox="0 0 15 16"><path d="M7.5 1a4.5 4.5 0 0 1 4.5 4.5V10l2 2.5H1L3 10V5.5A4.5 4.5 0 0 1 7.5 1z" fill="#fff"/><circle cx="7.5" cy="14" r="1.8" fill="#fff"/></svg>
      <span>Allowance renews in 18 days</span>
    </div>
  </footer>
</section>

</body>
</html>
```